ROLL-UP DESIGN FOR SUPERMARKET DELIVERY

We need the graphic design of a roll-up with measurements 200 cm height x cm 85 width, for a supermarket delivery service.

The main logo "The Bluhaven" either color version or black version must be present very visible on the design.

the second logo attached 'CASPANIMARKET' must also be present but smaller on the design.

the following text must be present on the design: CONSEGNA STESSO GIORNO.

Printing instruction attached must be respected.

Target Market(s)

HIGH END ITALIAN AND EUROPEAN SUPERMARKET CLIENTELE

Industry/Entity Type

FOOD DELIVERY

Requirements
Must have
• LOGOS ATTACHED
Nice to have
• PHOTOS OF SEA, SARDINIA, LUXURY DELIVERY, YACHTS

```html
<!DOCTYPE html>
<html lang="it">
<head>
<meta charset="utf-8">
<title>The Bluhaven – Consegna stesso giorno</title>
<link href="https://fonts.googleapis.com/css2?family=Montserrat:wght@600;700;800&display=swap" rel="stylesheet">
<style>
  :root {
    --sky-top: #3f84d2;
    --sky-low: #7db6e8;
    --sea-deep: #1d78c6;
    --sea-mid: #4fb9df;
    --sea-shallow: #b9e3e4;
    --sea-shore: #e4f4ef;
    --brand-yellow: #f9bf3b;
    --band-blue: rgba(44, 110, 200, 0.55);
    --band-yellow: rgba(255, 205, 120, 0.8);
    --band-edge: rgba(220, 245, 245, 0.7);
    --footer-grey: #939598;
    --white: #ffffff;
    --deep-blue: #1f5fa8;
  }
  html, body {
    margin: 0;
    padding: 0;
    width: 1200px;
    height: 3102px;
    overflow: hidden;
    background: var(--white);
  }
  .rollup {
    position: relative;
    width: 1200px;
    height: 3102px;
    overflow: hidden;
    font-family: "Montserrat", Arial, sans-serif;
  }
  .sea-backdrop {
    position: absolute;
    left: 0; top: 0;
    width: 1200px; height: 2820px;
    background: linear-gradient(180deg,
      var(--sky-top) 0px,
      var(--sky-low) 860px,
      var(--sea-deep) 890px,
      var(--sea-deep) 960px,
      var(--sea-mid) 1250px,
      var(--sea-shallow) 2200px,
      var(--sea-shore) 2820px);
  }
  .diagonal-bands {
    position: absolute;
    left: 0; top: 0;
    width: 1200px; height: 2820px;
  }
  .brand-header {
    position: absolute;
    left: 0; top: 0;
    width: 1200px;
  }
  .brand-dot {
    position: absolute;
    left: 262px; top: 100px;
    width: 80px; height: 80px;
    border: 5px solid var(--white);
    border-radius: 50%;
    box-sizing: border-box;
  }
  .brand-name {
    position: absolute;
    left: 400px; top: 72px;
    margin: 0;
    font-weight: 700;
    font-size: 100px;
    line-height: 1;
    letter-spacing: -2px;
    color: var(--brand-yellow);
    white-space: nowrap;
  }
  .brand-tagline {
    position: absolute;
    left: 470px; top: 198px;
    margin: 0;
    font-weight: 700;
    font-size: 32px;
    letter-spacing: 7px;
    color: var(--white);
    white-space: nowrap;
  }
  .headline {
    position: absolute;
    left: 74px; top: 560px;
    margin: 0;
    font-weight: 800;
    font-size: 170px;
    line-height: 178px;
    letter-spacing: 1px;
    color: var(--white);
    text-transform: uppercase;
  }
  .headline span { display: block; }
  .market-signature {
    position: absolute;
    right: 44px; top: 2670px;
    text-align: right;
    color: var(--deep-blue);
    font-weight: 800;
  }
  .market-name {
    display: block;
    font-size: 44px;
    line-height: 50px;
    letter-spacing: 0.5px;
    text-transform: uppercase;
    white-space: nowrap;
  }
  .market-name::before {
    content: "";
    display: inline-block;
    width: 26px; height: 26px;
    margin-right: 14px;
    background: var(--deep-blue);
    vertical-align: 2px;
  }
  .market-tagline {
    display: block;
    font-size: 22px;
    line-height: 30px;
    white-space: nowrap;
  }
  .footer-band {
    position: absolute;
    left: 0; top: 2820px;
    width: 1200px; height: 282px;
    background: var(--footer-grey);
  }
</style>
</head>
<body>
<main class="rollup">
  <div class="sea-backdrop" role="img" aria-label="Foto di mare cristallino sardo con cielo azzurro, acqua turchese e fondale chiaro"></div>

  <svg class="diagonal-bands" viewBox="0 0 1200 2820" aria-hidden="true">
    <polygon points="1200,1115 1200,1160 0,2340 0,2300" fill="var(--band-edge)"/>
    <polygon points="1200,693 1200,1120 0,2300 0,1886" fill="var(--band-blue)"/>
    <polygon points="1200,1160 1200,1605 0,2770 0,2335" fill="var(--band-yellow)"/>
    <polygon points="1200,1605 1200,1628 0,2795 0,2770" fill="var(--band-edge)"/>
    <polygon points="1200,1628 1200,2048 440,2820 0,2820 0,2795" fill="var(--band-blue)"/>
  </svg>

  <header class="brand-header">
    <span class="brand-dot"></span>
    <h1 class="brand-name">The Bluhaven</h1>
    <p class="brand-tagline">ORDINA E RILASSATI</p>
  </header>

  <h2 class="headline">
    <span>Consegna</span>
    <span>Stesso</span>
    <span>Giorno</span>
  </h2>

  <div class="market-signature">
    <span class="market-name">Caspanimarket</span>
    <span class="market-tagline">Spesa a domicilio</span>
  </div>

  <div class="footer-band"></div>
</main>
</body>
</html>
```